Sturdyflow Mechanical - Letterhead

We are a plumbing and hvac company based in Calgary. This letterhead will be on our quotes, invoices, preventative maintenance proposals etc.

```html
<!DOCTYPE html>
<html lang="en">
<head>
<meta charset="utf-8">
<title>Sturdyflow Mechanical – Letterhead</title>
<link href="https://fonts.googleapis.com/css2?family=Montserrat:wght@400;600;800&display=swap" rel="stylesheet">
<style>
  :root{
    --brand-blue:#1b6fb5;
    --brand-orange:#f15a29;
    --ink:#1d1d1d;
    --paper:#ffffff;
    --backdrop:#f2f2f2;
    --watermark:#fdf1ec;
  }
  *{margin:0;padding:0;box-sizing:border-box}
  html,body{width:1200px;height:943px;overflow:hidden}
  body{background:var(--backdrop);font-family:"Montserrat",sans-serif;position:relative}
  .sheet{position:absolute;top:130px;width:482px;height:683px;background:var(--paper);overflow:hidden;border:1px solid #d8d8d8}
  .sheet--blank{left:91px}
  .sheet--letter{left:628px}
  .brand{position:absolute;left:24px;top:42px;width:152px;display:flex;align-items:center;gap:6px}
  .brand__dot{width:14px;height:14px;border-radius:50%;background:var(--brand-orange);flex:none}
  .brand__name{font-weight:800;font-size:15px;line-height:1.1;color:var(--brand-blue)}
  .contact{position:absolute;left:292px;top:28px;font-size:10px;line-height:11.6px;color:var(--brand-blue);list-style:none}
  .contact li{display:flex;gap:5px;align-items:flex-start}
  .contact li+li{margin-top:1px}
  .contact .contact__address{margin-bottom:4px}
  .contact svg{width:8px;height:8px;margin-top:2px;flex:none;fill:var(--brand-orange)}
  .watermark{position:absolute;left:120px;top:222px;width:240px;height:240px;border-radius:50%;background:var(--watermark)}
  .band{position:absolute;left:0;width:100%}
  .band--orange{top:655px;height:10px;background:var(--brand-orange)}
  .band--blue{top:668px;height:15px;background:var(--brand-blue)}
  .letter{position:absolute;left:51px;width:380px;font-size:9.5px;line-height:11.3px;color:var(--ink)}
  .letter__recipient{top:166px}
  .letter__subject{top:239px;font-weight:600;font-size:11.3px}
  .letter__body{top:280px;text-align:justify}
  .letter__body p+p{margin-top:11.3px}
  .letter__body p:first-child{text-indent:28px}
  .letter__closing{top:496px}
  .signature{position:absolute;left:51px;top:524px;width:122px;height:32px;background:#ececec;border-radius:3px}
</style>
</head>
<body>

<section class="sheet sheet--blank">
  <div class="brand"><span class="brand__dot"></span><span class="brand__name">Sturdyflow Mechanical</span></div>
  <ul class="contact">
    <li class="contact__address"><svg viewBox="0 0 10 10"><path d="M5 0a3.5 3.5 0 0 0-3.5 3.5C1.5 6 5 10 5 10s3.5-4 3.5-6.5A3.5 3.5 0 0 0 5 0zm0 5a1.4 1.4 0 1 1 0-2.8A1.4 1.4 0 0 1 5 5z"/></svg><span>2-4715 58 Ave SE, Calgary<br>AB T2C 4K8, Canada</span></li>
    <li><svg viewBox="0 0 10 10"><path d="M2 0l2 2.5-1 1.2c.6 1.3 1.6 2.3 2.9 2.9l1.2-1L10 7.5 8.7 9.6C4.5 9.8.2 5.5.4 1.3z"/></svg><span>(403) 555-0187</span></li>
    <li><svg viewBox="0 0 10 10"><path d="M0 2h10v6H0zM0 2l5 3.5L10 2" stroke="#fff" stroke-width=".8"/></svg><span>info@sturdyflowmech.com</span></li>
    <li><svg viewBox="0 0 10 10"><circle cx="5" cy="5" r="5"/></svg><span>www.sturdyflowmech.com</span></li>
  </ul>
  <div class="watermark" aria-hidden="true"></div>
  <div class="band band--orange"></div>
  <div class="band band--blue"></div>
</section>

<section class="sheet sheet--letter">
  <div class="brand"><span class="brand__dot"></span><span class="brand__name">Sturdyflow Mechanical</span></div>
  <ul class="contact">
    <li class="contact__address"><svg viewBox="0 0 10 10"><path d="M5 0a3.5 3.5 0 0 0-3.5 3.5C1.5 6 5 10 5 10s3.5-4 3.5-6.5A3.5 3.5 0 0 0 5 0zm0 5a1.4 1.4 0 1 1 0-2.8A1.4 1.4 0 0 1 5 5z"/></svg><span>2-4715 58 Ave SE, Calgary<br>AB T2C 4K8, Canada</span></li>
    <li><svg viewBox="0 0 10 10"><path d="M2 0l2 2.5-1 1.2c.6 1.3 1.6 2.3 2.9 2.9l1.2-1L10 7.5 8.7 9.6C4.5 9.8.2 5.5.4 1.3z"/></svg><span>(403) 555-0187</span></li>
    <li><svg viewBox="0 0 10 10"><path d="M0 2h10v6H0zM0 2l5 3.5L10 2" stroke="#fff" stroke-width=".8"/></svg><span>info@sturdyflowmech.com</span></li>
    <li><svg viewBox="0 0 10 10"><circle cx="5" cy="5" r="5"/></svg><span>www.sturdyflowmech.com</span></li>
  </ul>
  <div class="watermark" aria-hidden="true"></div>

  <div class="letter letter__recipient">To,<br>Director<br>Meadowlark Land and Farm<br>Texas</div>
  <div class="letter letter__subject">Sub: Lorem ipsum dolor sit amet, consectetur adipiscing elit.</div>
  <div class="letter letter__body">
    <p>Lorem ipsum dolor sit amet, consectetur adipiscing elit, sed do eiusmod tempor incididunt ut labore et dolore magna aliqua. Quis ipsum suspendisse ultrices gravida. Risus commodo viverra maecenas accumsan lacus vel facilisis.</p>
    <p>Lorem ipsum dolor sit amet, consectetur adipiscing elit, sed do eiusmod tempor incididunt ut labore et dolore magna aliqua. Quis ipsum suspendisse ultrices gravida. Risus commodo viverra maecenas accumsan lacus vel facilisis. Lorem ipsum dolor sit amet, consectetur adipiscing elit, sed do eiusmod tempor incididunt ut labore et dolore magna aliqua. Quis ipsum suspendisse ultrices gravida. Risus commodo viverra maecenas accumsan lacus vel facilisis. Lorem ipsum dolor sit amet, consectetur adipiscing elit, sed do eiusmod tempor incididunt ut labore et dolore magna aliqua. Quis ipsum suspendisse ultrices gravida. Risus commodo viverra maecenas accumsan lacus vel facilisis.</p>
    <p>Lorem ipsum dolor sit amet, consectetur adipiscing elit, sed do eiusmod tempor incididunt ut labore et dolore magna aliqua.</p>
  </div>
  <div class="letter letter__closing">With Regards</div>
  <div class="signature" role="img" aria-label="Handwritten signature of the sender"></div>

  <div class="band band--orange"></div>
  <div class="band band--blue"></div>
</section>

</body>
</html>
```